Business Card

THIS IS THE CARD INFORMATION
DEVELOPMENT I FINANCING I PROPERTY MANAGEMENT
DANIEL ORTEGA
3182 NW 97th Avenue
Palm Hollow, FL 33418
Telephone I 877.452.6184
Facsimile I 877.452.6127
Industry/Entity Type
Business

```html
<!DOCTYPE html>
<html lang="en">
<head>
<meta charset="utf-8">
<title>Navarro Ruiz &amp; Company – Business Card</title>
<link href="https://fonts.googleapis.com/css2?family=Roboto+Condensed:wght@400;700&family=Roboto:wght@400;500&display=swap" rel="stylesheet">
<style>
  :root {
    --backdrop: #e7e4df;
    --card: #2c2c2e;
    --magenta: #a3239c;
    --magenta-soft: #b63fae;
    --white: #ffffff;
    --light: #e6e6e6;
  }
  * { margin: 0; padding: 0; box-sizing: border-box; }
  html, body {
    width: 1200px;
    height: 1000px;
    overflow: hidden;
    background: var(--backdrop);
  }
  .canvas {
    position: relative;
    width: 1200px;
    height: 1000px;
  }
  .card {
    position: absolute;
    left: 150px;
    top: 245px;
    width: 900px;
    height: 510px;
    background: var(--card);
    border-top: 14px solid var(--magenta);
    border-bottom: 14px solid var(--magenta);
    box-shadow: 0 14px 30px rgba(0, 0, 0, 0.25);
    font-family: "Roboto", Arial, sans-serif;
    color: var(--white);
  }
  .brand {
    position: absolute;
    left: 80px;
    top: 170px;
    display: flex;
    align-items: center;
    gap: 26px;
  }
  .brand-dot {
    width: 120px;
    height: 120px;
    border-radius: 50%;
    background: var(--magenta);
    flex: none;
  }
  .brand-name {
    font-family: "Roboto Condensed", "Arial Narrow", sans-serif;
    font-weight: 700;
    color: var(--white);
    font-size: 46px;
    line-height: 1;
    letter-spacing: 0.5px;
  }
  .brand-name span {
    display: block;
    font-size: 26px;
    margin-top: 8px;
    letter-spacing: 2px;
  }
  .details {
    position: absolute;
    left: 520px;
    top: 70px;
  }
  .person-name {
    font-family: "Roboto Condensed", "Arial Narrow", sans-serif;
    font-weight: 700;
    color: var(--magenta-soft);
    font-size: 30px;
    letter-spacing: 0.5px;
  }
  .person-title {
    font-size: 20px;
    color: var(--white);
    margin-top: 2px;
  }
  .contacts {
    list-style: none;
    margin: 26px 0 0 48px;
  }
  .contact {
    display: flex;
    align-items: center;
    gap: 14px;
    font-size: 17px;
    color: var(--light);
    margin-bottom: 14px;
  }
  .contact-icon {
    width: 30px;
    height: 30px;
    border-radius: 50%;
    background: var(--magenta);
    display: flex;
    align-items: center;
    justify-content: center;
    flex: none;
  }
  .office {
    margin: 14px 0 0 48px;
  }
  .office-name {
    font-family: "Roboto Condensed", "Arial Narrow", sans-serif;
    font-weight: 700;
    color: var(--magenta-soft);
    font-size: 21px;
  }
  .office-address {
    font-size: 17px;
    color: var(--light);
    margin-top: 4px;
  }
</style>
</head>
<body>
<main class="canvas">
  <article class="card">
    <div class="brand">
      <div class="brand-dot"></div>
      <div class="brand-name">NAVARRO RUIZ<span>&amp; COMPANY</span></div>
    </div>

    <section class="details">
      <h1 class="person-name">YOUR NAME</h1>
      <p class="person-title">Title</p>

      <ul class="contacts">
        <li class="contact">
          <span class="contact-icon">
            <svg width="16" height="16" viewBox="0 0 24 24" aria-hidden="true">
              <path fill="#fff" d="M6.6 10.8a15.1 15.1 0 0 0 6.6 6.6l2.2-2.2a1 1 0 0 1 1-.25 11.4 11.4 0 0 0 3.6.57 1 1 0 0 1 1 1V20a1 1 0 0 1-1 1A17 17 0 0 1 3 4a1 1 0 0 1 1-1h3.5a1 1 0 0 1 1 1c0 1.25.2 2.45.57 3.57a1 1 0 0 1-.25 1z"/>
            </svg>
          </span>
          123 456 789
        </li>
        <li class="contact">
          <span class="contact-icon">
            <svg width="16" height="16" viewBox="0 0 24 24" aria-hidden="true">
              <path fill="#fff" d="M3 6h18v12H3z"/>
              <path fill="none" stroke="#a3239c" stroke-width="1.8" d="M3 6l9 7 9-7"/>
            </svg>
          </span>
          yourname@navarroruiz.com
        </li>
        <li class="contact">
          <span class="contact-icon">
            <svg width="18" height="18" viewBox="0 0 24 24" aria-hidden="true">
              <g fill="none" stroke="#fff" stroke-width="1.6">
                <circle cx="12" cy="12" r="9"/>
                <ellipse cx="12" cy="12" rx="4" ry="9"/>
                <path d="M3 12h18M5 7h14M5 17h14"/>
              </g>
            </svg>
          </span>
          www.navarroruiz.com
        </li>
      </ul>

      <div class="office">
        <p class="office-name">Navarro Ruiz &amp; Company</p>
        <p class="office-address">P.O.Box 123 City, Country 1234</p>
      </div>
    </section>
  </article>
</main>
</body>
</html>
```